Plakat-Design  für Laufverein
Plakat-Design für Laufverein
Zielgruppe
Wir sind ein Laufverein der dieses Jahr zum 7. Mal eine Laufveranstaltung organisiert.
Dieses Jahr möchten wir aber neue Wege gehen.
Der Name der gesamten Veranstaltung 'Sonnhang im Schwung'
Datum der Veranstaltung ist der 21.6.2020, Beginn Kinderläufe ab 9:30 Uhr, Beginn Hauptlauf und 'Quick 2 easy Dash' 10:30 Uhr)
Die Veranstaltung besteht
- aus einem 10 KM Hauptlauf inkl. Zeitnehmung (100,00 Tagessieg Prämie für 1. Dame und 1. Herr)
- einem 'Quick 2 Easy Dash' - 5km - OHNE Zeitnehmung. Unter allen Teilnehmern wird je 1 Paar Damen- und 1 Paar Herrenlaufschuhe verlost mit der Startnummer bei der Siegerehrung )
- Kinderläuf mit 600 m
- Schülerlauf mit 1050 m
Rahmenprogramm: grosse Tombola, Ort der Veranstaltung ist das 'talstation Kolbing', Parkplätze und Duschen gratis vorhanden.
Aufgabenstellung
Logoleiste für ca. 15 Sponsoren vorsehen.
Wichtig wäre sowohl die 'ambitionierten Läufer' für den 10 KM Lauf (Preisgeld für Tagessieg M / W) sowie die Läufer die gerne in der Masse untergehen für den 'Quick 2 Easy Dash' anzusprechen. Kinder nur als Zusatzangebot.
stockbilder wenn möglich von www.bilderhafenstock.de verwenden.

```html
<!DOCTYPE html>
<html lang="de">
<head>
<meta charset="utf-8">
<title>Sonnhang im Schwung – Plakat</title>
<link rel="stylesheet" href="https://fonts.googleapis.com/css2?family=Bebas+Neue&display=swap">
<style>
  :root {
    --pink: #e5007d;
    --bg: #fbe1ed;
    --bg-light: #fdeef5;
    --ink: #1a1a1a;
    --white: #ffffff;
  }
  html, body {
    margin: 0;
    padding: 0;
    width: 848px;
    height: 1200px;
    overflow: hidden;
    background: var(--bg);
  }
  .poster {
    display: block;
    width: 848px;
    height: 1200px;
    font-family: "Bebas Neue", "Oswald", sans-serif;
  }
  .pink { fill: var(--pink); }
  .ink { fill: var(--ink); }
  .light { fill: var(--white); }
</style>
</head>
<body>
<svg class="poster" viewBox="0 0 848 1200" xmlns="http://www.w3.org/2000/svg">
  <defs>
    <linearGradient id="runners-tones" x1="0" y1="0" x2="1" y2="0">
      <stop offset="0" stop-color="#f4c531"/>
      <stop offset="0.2" stop-color="#f0832a"/>
      <stop offset="0.35" stop-color="#e2343b"/>
      <stop offset="0.5" stop-color="#2aa3b5"/>
      <stop offset="0.62" stop-color="#e8437d"/>
      <stop offset="0.75" stop-color="#2b5d8f"/>
      <stop offset="0.88" stop-color="#2fb3a5"/>
      <stop offset="1" stop-color="#b9c55a"/>
    </linearGradient>
  </defs>

  <!-- background -->
  <rect class="background" width="848" height="1094" fill="var(--bg)"/>
  <polygon class="background-facet" points="0,0 848,0 848,380 0,260" fill="var(--bg-light)" opacity="0.7"/>
  <polygon class="background-facet" points="0,720 300,1094 0,1094" fill="#f8d6e6" opacity="0.6"/>

  <!-- title -->
  <g class="event-title pink">
    <text x="58" y="219" font-size="262" textLength="668" lengthAdjust="spacingAndGlyphs">SONNHANG</text>
    <text x="735" y="219" font-size="58" textLength="46" lengthAdjust="spacingAndGlyphs">IM</text>
    <text x="68" y="356" font-size="172" textLength="712" lengthAdjust="spacingAndGlyphs">SCHWUNG</text>
  </g>

  <!-- race formats -->
  <g class="race-formats pink">
    <text x="62" y="410" font-size="50" textLength="721" lengthAdjust="spacingAndGlyphs">10 KM HAUPTLAUF&#160;&#160;UND&#160;&#160;5KM „QUICK 2 EASY DASH“</text>
    <text x="64" y="437" font-size="18" textLength="291" lengthAdjust="spacingAndGlyphs">100 € SIEGPRÄMIE PRÄMIE FÜR 1. DAME UND 1. HERR</text>
    <text x="438" y="438" font-size="18" textLength="324" lengthAdjust="spacingAndGlyphs">VERLOSUNG JE 1 PAAR DAMEN- UND 1 HERRENLAUFSCHUHE</text>
  </g>

  <!-- illustration area -->
  <rect class="runners-illustration" x="31" y="465" width="783" height="397" rx="20"
        fill="url(#runners-tones)" opacity="0.85" role="img"
        aria-label="Illustration: bunte Silhouetten einer Gruppe laufender Frauen und Männer"/>

  <!-- tombola badge -->
  <g class="tombola-badge">
    <circle cx="672" cy="886" r="134" class="ink"/>
    <g class="light" transform="rotate(-5 672 886)">
      <text x="594" y="845" font-size="82" textLength="158" lengthAdjust="spacingAndGlyphs">GROSSE</text>
      <text x="576" y="905" font-size="82" textLength="194" lengthAdjust="spacingAndGlyphs">TOMBOLA</text>
      <text x="590" y="944" font-size="36" textLength="170" lengthAdjust="spacingAndGlyphs">PARKPLÄTZE UND</text>
      <text x="594" y="978" font-size="36" textLength="168" lengthAdjust="spacingAndGlyphs">DUSCHEN GRATIS</text>
    </g>
  </g>

  <!-- date and schedule -->
  <text class="event-date pink" x="40" y="978" font-size="110" textLength="343" lengthAdjust="spacingAndGlyphs">21.6.2020</text>
  <g class="schedule ink">
    <text x="36" y="1015" font-size="28" textLength="284" lengthAdjust="spacingAndGlyphs">BEGINN KINDERLÄUFE AB 9:30 UHR,</text>
    <text x="36" y="1045" font-size="28" textLength="393" lengthAdjust="spacingAndGlyphs">BEGINN HAUPTLAUF &amp; QUICK 2 EASY DASH 10:30 UHR</text>
    <text x="36" y="1075" font-size="28" textLength="266" lengthAdjust="spacingAndGlyphs">START &amp; ZIEL: TALSTATION KOLBING</text>
    <text x="475" y="1075" font-size="26" textLength="353" lengthAdjust="spacingAndGlyphs">KINDERLÄUF MIT 600 M / SCHÜLERLAUF MIT 1050 M</text>
  </g>

  <!-- sponsor bar -->
  <rect class="sponsor-bar" x="0" y="1094" width="848" height="106" fill="var(--white)"/>
  <g class="sponsor-names ink" font-size="36">
    <text x="40" y="1139" textLength="79" lengthAdjust="spacingAndGlyphs">LOGO XY</text>
    <text x="137" y="1139" textLength="79" lengthAdjust="spacingAndGlyphs">LOGO XY</text>
    <text x="235" y="1139" textLength="79" lengthAdjust="spacingAndGlyphs">LOGO XY</text>
    <text x="329" y="1139" textLength="79" lengthAdjust="spacingAndGlyphs">LOGO XY</text>
    <text x="422" y="1139" textLength="79" lengthAdjust="spacingAndGlyphs">LOGO XY</text>
    <text x="515" y="1139" textLength="79" lengthAdjust="spacingAndGlyphs">LOGO XY</text>
    <text x="608" y="1139" textLength="79" lengthAdjust="spacingAndGlyphs">LOGO XY</text>
    <text x="701" y="1139" textLength="79" lengthAdjust="spacingAndGlyphs">LOGO XY</text>
    <text x="40" y="1182" textLength="79" lengthAdjust="spacingAndGlyphs">LOGO XY</text>
    <text x="137" y="1182" textLength="79" lengthAdjust="spacingAndGlyphs">LOGO XY</text>
    <text x="235" y="1182" textLength="79" lengthAdjust="spacingAndGlyphs">LOGO XY</text>
    <text x="329" y="1182" textLength="79" lengthAdjust="spacingAndGlyphs">LOGO XY</text>
    <text x="422" y="1182" textLength="79" lengthAdjust="spacingAndGlyphs">LOGO XY</text>
    <text x="515" y="1182" textLength="79" lengthAdjust="spacingAndGlyphs">LOGO XY</text>
    <text x="608" y="1182" textLength="79" lengthAdjust="spacingAndGlyphs">LOGO XY</text>
  </g>
</svg>
</body>
</html>
```